Torrelin Business Card Design - double sided -plumbing local plumbing company

We have a Plumbing company where the design was create through Sketch Hive. We would now like a business card designed as well. We want it to be in the colour version of the logo.

Details below for the card.

Phone Number: 0438 615 247
Email: info@torrelinplumbing.example.au
Website: https://torrelinplumbing.example.au
We really want a sophisticated design that stand out from the other- informative and timeless.

Target Market(s)

local Canberra market

Industry/Entity Type

Plumbing, gas fitting, hot water

Contact Information for Business Card

Phone number, email, logo and "Supplying all your heating, cooling and hot water needs"

Requirements
Must have
• bust be colourful, must also be though about it being printed on a magnet. must Vex with the logo - I dont want the logo and information chucked onto a white canvas I would prefer it to be smooth and look purposeful

```html
<!DOCTYPE html>
<html lang="en">
<head>
<meta charset="utf-8">
<title>Torrelin Plumbing – Business Card</title>
<link rel="stylesheet" href="https://fonts.googleapis.com/css2?family=Montserrat:ital,wght@0,400;0,600;0,800;1,400&display=swap">
<style>
  :root {
    --bg: #e9eaec;
    --card-white: #f4f4f5;
    --brand-blue: #1d9ee0;
    --brand-orange: #f0a233;
    --ink: #3a3d42;
    --white: #ffffff;
  }
  * { box-sizing: border-box; margin: 0; padding: 0; }
  html, body {
    width: 1200px; height: 802px; overflow: hidden;
    background: var(--bg);
    font-family: "Montserrat", sans-serif;
  }
  .stage {
    position: relative; width: 1200px; height: 802px;
    display: flex; align-items: center; justify-content: center; gap: 40px;
  }
  .card {
    position: relative; width: 520px; height: 317px;
    border-radius: 26px; overflow: hidden;
    box-shadow: 0 10px 30px rgba(0,0,0,0.12);
  }
  .card--front { background: var(--card-white); }
  .card--back { background: var(--brand-blue); }

  .front__panel {
    position: absolute; top: 0; right: 0; bottom: 0; left: 255px;
    background: var(--brand-blue);
  }
  .front__name-tab {
    position: absolute; top: 40px; left: 228px; width: 210px; height: 48px;
    background: var(--brand-orange);
    clip-path: polygon(8% 0, 100% 0, 100% 100%, 0 100%);
    color: var(--white); text-align: center;
    display: flex; flex-direction: column; justify-content: center;
    padding-left: 14px;
  }
  .front__name { font-weight: 600; font-size: 13px; letter-spacing: 0.5px; }
  .front__role { font-size: 7.5px; margin-top: 2px; }

  .brand-name {
    position: absolute; left: 26px; top: 132px;
    font-weight: 800; font-size: 32px; color: var(--brand-blue);
    letter-spacing: 0.5px;
  }

  .contact-list {
    position: absolute; left: 30px; top: 226px; list-style: none;
    font-size: 9.5px; color: var(--ink);
  }
  .contact-list li {
    display: flex; align-items: center; gap: 8px; height: 16px;
  }
  .contact-icon {
    width: 11px; height: 11px; background: var(--brand-blue);
    display: inline-flex; align-items: center; justify-content: center;
  }
  .contact-icon svg { width: 8px; height: 8px; }

  .tagline {
    position: absolute; right: 32px; top: 196px; width: 190px;
    color: var(--white); font-style: italic; font-size: 10px;
    line-height: 1.45; text-align: right;
  }
</style>
</head>
<body>
<main class="stage">
  <section class="card card--front" aria-label="Business card front">
    <div class="front__panel"></div>
    <div class="front__name-tab">
      <span class="front__name">JOHN DOE</span>
      <span class="front__role">Director / Owner</span>
    </div>

    <div class="brand-name">TORRELIN</div>

    <ul class="contact-list">
      <li>
        <span class="contact-icon">
          <svg viewBox="0 0 10 10"><path d="M2 1 L4 1 L4.6 3 L3.4 3.8 Q4.4 5.8 6.2 6.6 L7 5.4 L9 6 L9 8 Q5 9 1.6 5 Q1 3 2 1 Z" fill="#fff"/></svg>
        </span>
        0438 615 247
      </li>
      <li>
        <span class="contact-icon">
          <svg viewBox="0 0 10 10"><rect x="1" y="2.5" width="8" height="5.5" fill="none" stroke="#fff" stroke-width="1"/><path d="M1 2.5 L5 6 L9 2.5" fill="none" stroke="#fff" stroke-width="1"/></svg>
        </span>
        info@torrelinplumbing.example.au
      </li>
      <li>
        <span class="contact-icon">
          <svg viewBox="0 0 10 10"><circle cx="5" cy="5" r="3.8" fill="none" stroke="#fff" stroke-width="0.9"/><ellipse cx="5" cy="5" rx="1.6" ry="3.8" fill="none" stroke="#fff" stroke-width="0.8"/><path d="M1.2 5 H8.8" stroke="#fff" stroke-width="0.8"/></svg>
        </span>
        www.example.com
      </li>
    </ul>

    <p class="tagline">"Supplying all your heating, cooling and hot water needs"</p>
  </section>

  <section class="card card--back" aria-label="Business card back"></section>
</main>
</body>
</html>
```